High Tech Real Estate Startup needs a business card

We are developing an innovative real estate marketing product based around advanced search and virtual reality.

We talk to people, we need business cards.

Target Market(s)

The target market is technology professionals and realtors.

Contact Information for Business Card

The information to be included will include

Name
Title
Phone Number
E-mail Address
www.quelzo.com

It should use simple iconography for each one of those fields.

Font styles to use
Other font styles liked:
• Co, Jubilat, Avenir

Colors

Designer to choose colors to be used in the design.

Requirements
Must have
• Clean aesthetic,
• Good use of negative space.
• It should use our company logo, shown in the attached file. It is able to use the negative of that logo (coloured font and white background) and I have attached other acceptable accent colours in a swatch file.
Should not have
• Should not be too busy
• No extraneous text (slogans, tag lines etc)

```html
<!DOCTYPE html>
<html lang="en">
<head>
<meta charset="utf-8">
<title>Quelzo Business Card</title>
<link href="https://fonts.googleapis.com/css2?family=Montserrat:wght@500&family=Roboto:wght@400&display=swap" rel="stylesheet">
<style>
  :root {
    --teal: #14bcc0;
    --ink: #1f1f1f;
    --paper: #ffffff;
    --backdrop: #dcdcdc;
  }
  * { margin: 0; padding: 0; box-sizing: border-box; }
  html, body { width: 1200px; height: 930px; overflow: hidden; background: var(--backdrop); }
  .stage { position: relative; width: 1200px; height: 930px; }

  .card {
    position: absolute;
    width: 560px;
    height: 320px;
    border-radius: 18px;
    overflow: hidden;
  }
  .card--front { left: 70px; top: 110px; background: var(--teal); display: flex; align-items: center; justify-content: center; }
  .card--back { left: 570px; top: 500px; background: var(--paper); }

  .brand-name {
    font-family: "Montserrat", sans-serif;
    font-weight: 500;
    letter-spacing: 2px;
    line-height: 1;
  }
  .card--front .brand-name { color: var(--paper); font-size: 74px; }
  .card--back .brand-name { position: absolute; left: 40px; top: 118px; color: var(--teal); font-size: 54px; }

  .wave { position: absolute; left: 0; top: 0; width: 560px; height: 320px; }

  .person { position: absolute; right: 34px; top: 112px; text-align: right; }
  .person__name { font-family: "Montserrat", sans-serif; font-weight: 500; color: var(--teal); font-size: 21px; text-transform: uppercase; letter-spacing: 0.5px; }
  .person__title { font-family: "Roboto", sans-serif; color: var(--ink); font-size: 13px; margin-top: 2px; }

  .divider { position: absolute; left: 40px; right: 34px; top: 182px; height: 1.5px; background: var(--teal); }

  .contact-list { position: absolute; left: 40px; top: 200px; list-style: none; font-family: "Roboto", sans-serif; font-size: 15px; color: var(--ink); }
  .contact-list li { display: flex; align-items: center; gap: 9px; line-height: 24px; }
  .contact-list svg { width: 11px; height: 11px; flex: none; }

  .address { position: absolute; right: 34px; top: 196px; text-align: right; font-family: "Roboto", sans-serif; font-size: 14px; line-height: 19px; color: var(--ink); }
</style>
</head>
<body>
<main class="stage">
  <section class="card card--front">
    <span class="brand-name">QUELZO</span>
  </section>

  <section class="card card--back">
    <svg class="wave" viewBox="0 0 560 320" aria-hidden="true">
      <path d="M0 0 H560 V40 C470 85 330 78 200 84 C110 88 40 100 0 120 Z" fill="var(--teal)"/>
      <path d="M0 128 C40 106 110 95 200 92 C330 86 470 92 560 46" fill="none" stroke="var(--ink)" stroke-width="9"/>
      <path d="M0 132 C40 110 110 99 200 96 C330 90 470 96 560 50" fill="none" stroke="var(--paper)" stroke-width="2"/>
      <path d="M0 172 C20 130 70 110 190 104 C110 112 40 130 0 172 Z" fill="var(--teal)"/>
    </svg>

    <span class="brand-name">QUELZO</span>

    <div class="person">
      <p class="person__name">Daniel Reyes</p>
      <p class="person__title">Director</p>
    </div>

    <div class="divider"></div>

    <ul class="contact-list">
      <li>
        <svg viewBox="0 0 12 12"><path d="M2.5 1 L4.5 1 L5.2 3.5 L4 4.5 C4.6 6 6 7.4 7.5 8 L8.5 6.8 L11 7.5 L11 9.5 C11 10.3 10.3 11 9.5 11 C5 11 1 7 1 2.5 C1 1.7 1.7 1 2.5 1 Z" fill="var(--teal)"/></svg>
        +1-555-014-2297
      </li>
      <li>
        <svg viewBox="0 0 12 12"><rect x="1" y="2.5" width="10" height="7" fill="none" stroke="var(--teal)" stroke-width="1.2"/><path d="M1 2.5 L6 6.5 L11 2.5" fill="none" stroke="var(--teal)" stroke-width="1.2"/></svg>
        info@quelzo.com
      </li>
      <li>
        <svg viewBox="0 0 12 12"><circle cx="6" cy="6" r="5" fill="none" stroke="var(--teal)" stroke-width="1.2"/><ellipse cx="6" cy="6" rx="2.2" ry="5" fill="none" stroke="var(--teal)" stroke-width="1"/><path d="M1 6 H11" stroke="var(--teal)" stroke-width="1"/></svg>
        www.quelzo.com
      </li>
    </ul>

    <address class="address" style="font-style:normal">
      872 Maple Ridge Dr.<br>
      Brentwood, TN 37027
    </address>
  </section>
</main>
</body>
</html>
```